Bold Website Redesign for a Disruptive Training Brand

Brightmoor Labs is a bold, no-fluff sales & leadership training company powered by AI-driven practice and behavioral science. We’ve already built our website structure and copy in Craftly.io — now we need a designer to fully transform the visual design across all pages (Home, Approach, Programs, About, Contact).
We’re looking for a modern, memorable, high-performance aesthetic that blends human energy, science, and tech without feeling corporate or safe. Clean, bold typography, fluid layout, strong emotional hero moments, subtle motion, and imagery that mixes real people with abstract scientific/tech visuals.Because our clients are primarily North American, please ensure any human photography or AI-generated imagery reflects a North American business context and demographics (modern, diverse, and realistic).

Your job is visual redesign only — no coding required.
The final design must be practical to rebuild inside Craftly.io.

A full, detailed creative brief (plus logo files) is included in the uploaded files.
If you can bring a mix of edge, intelligence, and strong visual storytelling, we’d love to see your work.

Website is already built in Craftly.io at - https://brightmoor-website-tempdesign.craftly.app — structure is set, visuals need redesign.

```html
<!DOCTYPE html>
<html lang="en">
<head>
<meta charset="utf-8">
<title>Brightmoor Labs — Training that Practices Back</title>
<link href="https://fonts.googleapis.com/css2?family=Poppins:wght@400;500;600;700&family=Inter:wght@400;500&display=swap" rel="stylesheet">
<style>
:root{
  --navy:#0a1530;
  --navy-deep:#070f24;
  --ink:#111827;
  --blue:#3f6fc4;
  --blue-mid:#4a86d6;
  --cyan:#4cc3f0;
  --pale:#e6f0f9;
  --text:#2a2f3a;
  --white:#ffffff;
}
*{box-sizing:border-box;margin:0;padding:0}
html,body{width:1200px;height:3854px;overflow:hidden}
body{font-family:"Poppins",sans-serif;color:var(--text);background:var(--white);position:relative}
.grad-text{background:linear-gradient(90deg,var(--blue),var(--cyan));-webkit-background-clip:text;background-clip:text;color:transparent}
.btn{display:inline-flex;align-items:center;justify-content:center;gap:8px;border-radius:30px;font-family:"Poppins",sans-serif;font-weight:600;font-size:13px;letter-spacing:.2px;text-transform:uppercase;color:var(--white);background:linear-gradient(90deg,var(--blue),var(--cyan));position:absolute}
.btn.light{background:var(--white);color:var(--blue)}
section{position:absolute;left:0;width:1200px;overflow:hidden}
.divider{position:absolute;left:0;bottom:0;width:1200px;height:5px;background:linear-gradient(90deg,var(--blue),var(--cyan))}

/* hero */
.hero{top:0;height:720px;background:linear-gradient(100deg,#0b1633 0%,#0c1e45 40%,#0f3266 100%)}
.hero-visual{position:absolute;left:560px;top:0;width:640px;height:715px;background:radial-gradient(circle at 72% 30%,#d9f3ff 0%,#6cbdf2 9%,#2a63ae 30%,#10295a 60%,#0c1e45 85%)}
.hero-glow{position:absolute;left:0;top:380px;width:820px;height:335px;background:radial-gradient(ellipse at 25% 70%,rgba(70,150,230,.5),transparent 65%)}
.nav{position:absolute;top:22px;left:125px;width:1012px;height:50px;display:flex;align-items:center}
.brand{display:flex;align-items:center;gap:12px;color:var(--white);font-weight:600;font-size:17px;letter-spacing:2px;text-transform:uppercase}
.brand .mark{width:44px;height:44px;border-radius:50%;background:linear-gradient(135deg,var(--blue),var(--cyan))}
.nav ul{list-style:none;display:flex;gap:48px;margin-left:auto;margin-right:52px}
.nav li{color:var(--white);font-size:13px;font-weight:500}
.nav .btn{position:static;width:128px;height:36px;font-size:11px}
.hero h1{position:absolute;left:127px;top:186px;color:var(--white);font-size:69px;line-height:66px;font-weight:700}
.hero .lead{position:absolute;left:131px;top:343px;width:380px;color:var(--white);font-size:20px;line-height:27px;font-weight:600}
.hero .sub{position:absolute;left:131px;top:416px;width:390px;color:#dbe6f6;font-family:"Inter",sans-serif;font-size:14px;line-height:19px}

/* problem */
.problem{top:720px;height:730px;background:linear-gradient(180deg,#fff 0%,#f7f9fc 100%)}
.problem h2{position:absolute;top:117px;width:1200px;text-align:center;font-size:37px;line-height:52px;font-weight:600;color:var(--ink)}
.problem p{position:absolute;left:158px;top:306px;width:420px;font-size:22px;line-height:34.5px;color:var(--ink)}
.chart{position:absolute;left:653px;top:278px;width:467px;height:354px;border-radius:16px;background:var(--white);box-shadow:0 12px 30px rgba(40,70,120,.12);overflow:hidden}
.chart .lbl{position:absolute;font-size:11px;font-weight:600;line-height:14px;text-align:center;color:var(--ink)}

/* practice */
.practice{top:1450px;height:787px;background:linear-gradient(180deg,#e2eef8 0%,#eaf2fa 100%)}
.practice h2{position:absolute;left:155px;top:78px;font-size:42px;line-height:52px;font-weight:700;color:var(--ink)}
.practice .intro{position:absolute;left:588px;top:92px;width:460px;font-size:20px;line-height:27px;color:var(--ink)}
.person{position:absolute;left:122px;top:240px;width:440px;height:440px;border-radius:50%;background:radial-gradient(circle at 50% 40%,#f2ead8 0%,#e4e2ef 40%,#d4dcf3 75%,#c6d6f1 100%);box-shadow:0 0 0 3px rgba(120,180,240,.45),0 0 40px rgba(120,180,240,.3)}
.dash{position:absolute;background:var(--white);border-radius:6px;box-shadow:0 6px 16px rgba(40,70,120,.15);overflow:hidden}
.card{position:absolute;left:685px;width:400px;height:128px;border-radius:16px;background:var(--white);box-shadow:0 10px 24px rgba(40,70,120,.08)}
.card .icon{position:absolute;left:20px;top:23px;width:82px;height:82px;border-radius:50%;background:linear-gradient(135deg,var(--blue-mid),#1f4a93);display:flex;align-items:center;justify-content:center}
.card h3{position:absolute;left:121px;top:26px;font-size:17px;font-weight:500;color:var(--ink);letter-spacing:.5px}
.card p{position:absolute;left:122px;top:57px;width:230px;font-family:"Inter",sans-serif;font-size:13px;line-height:16px;color:#333}

/* team */
.team{top:2237px;height:668px;background:var(--white)}
.team-photo{position:absolute;left:560px;top:0;width:640px;height:663px;background:linear-gradient(100deg,#ffffff 0%,#e6e9ee 14%,#b9c2cc 34%,#8a7a6a 55%,#4b5563 75%,#6b7380 100%)}
.team h2{position:absolute;left:133px;top:133px;font-size:35px;line-height:51px;font-weight:600;color:var(--ink)}
.team p{position:absolute;left:133px;top:260px;width:460px;font-size:19px;line-height:31px;color:#333}

/* cta */
.cta{top:2905px;height:561px;background:radial-gradient(ellipse at 55% 85%,#1d5fa8 0%,#0c2a55 35%,var(--navy-deep) 70%)}
.cta h2{position:absolute;top:130px;width:1200px;text-align:center;color:var(--white);font-size:44px;line-height:52px;font-weight:600}

/* footer */
.footer{position:absolute;left:0;top:3466px;width:1200px;height:388px;background:linear-gradient(180deg,#0a1530 0%,#0e1d3d 100%);color:var(--white)}
.footer .brand{position:absolute;left:123px;top:100px}
.footer .tag{position:absolute;left:135px;top:162px;width:300px;font-family:"Inter",sans-serif;font-size:12px;line-height:19px;color:#dbe3f0}
.footer .copy{position:absolute;left:135px;top:239px;font-family:"Inter",sans-serif;font-size:11px;color:#c2cbdb}
.footer h4{position:absolute;font-size:14px;font-weight:600;letter-spacing:.3px}
.footer ul{position:absolute;list-style:none;font-family:"Inter",sans-serif;font-size:13px;line-height:27px;color:#e4eaf4}
.contact li{display:flex;gap:10px;align-items:flex-start;margin-bottom:12px;line-height:19px}
.social{position:absolute;left:955px;top:150px;display:flex;gap:6px}
.social span{width:30px;height:30px;border-radius:50%;background:var(--white);border:3px solid var(--blue-mid)}
</style>
</head>
<body>

<section class="hero">
  <div class="hero-visual" role="img" aria-label="Profile of a thoughtful person with glowing blue particle light streaming across the face"></div>
  <div class="hero-glow" role="img" aria-label="Flowing wave of blue glowing particles"></div>
  <nav class="nav">
    <div class="brand"><span class="mark"></span>Brightmoor Labs</div>
    <ul><li>HOME</li><li>APPROACH</li><li>PROGRAMS</li><li>ABOUT</li><li>CONTACT</li></ul>
    <span class="btn">Lets Talk</span>
  </nav>
  <h1>Training that<br>Practices Back</h1>
  <p class="lead">AI-driven sustainment that builds mastery — so you don't have to.</p>
  <p class="sub">You'll see measurable growth as your people turn insight into habit — automatically, sustainably, and without extra work for their leaders.</p>
  <span class="btn" style="left:130px;top:495px;width:196px;height:47px">See How We Do It</span>
  <span class="btn light" style="left:343px;top:493px;width:196px;height:47px">
    <svg width="18" height="16" viewBox="0 0 18 16"><path d="M2 2h10a2 2 0 0 1 2 2v5a2 2 0 0 1-2 2H6l-4 3V4a2 2 0 0 1 2-2z" fill="#3f6fc4"/></svg>Lets Talk</span>
  <div class="divider"></div>
</section>

<section class="problem">
  <h2>The real problem isn't your people<br><span class="grad-text">it's the forgetting curve.</span></h2>
  <p>Within a week, most training disappears. Leaders are left guessing who's using what they learned — and no one has time to fix it. We built Brightmoor Labs to make progress automatic, measurable, and real.</p>
  <span class="btn" style="left:160px;top:547px;width:196px;height:48px">See How We Do It</span>
  <div class="chart">
    <svg width="467" height="354" viewBox="0 0 467 354">
      <defs><linearGradient id="area" x1="0" y1="0" x2="1" y2="1"><stop offset="0" stop-color="#3f6fc4"/><stop offset="1" stop-color="#4cc3f0"/></linearGradient></defs>
      <g stroke="#e3e8ef" stroke-width="1">
        <path d="M0 30H467M0 60H467M0 90H467M0 120H467M0 150H467M0 180H467M0 210H467M0 240H467"/>
        <path d="M30 0V354M60 0V354M90 0V354M120 0V354M150 0V354M180 0V354M210 0V354M240 0V354M270 0V354M300 0V354M330 0V354M360 0V354M390 0V354M420 0V354M450 0V354"/>
      </g>
      <polyline points="0,128 55,140 120,128 185,154 255,140 308,164 400,160 467,164" fill="none" stroke="#8fb3df" stroke-width="2"/>
      <g fill="#3f6fc4"><circle cx="55" cy="140" r="4.5"/><circle cx="185" cy="154" r="4.5"/><circle cx="308" cy="164" r="4.5"/><circle cx="400" cy="160" r="4.5"/></g>
      <path d="M0 166 C60 210 120 240 220 248 C300 252 400 252 467 252 V354 H0Z" fill="url(#area)"/>
      <path d="M0 166 C60 210 120 240 220 248 C300 252 400 252 467 252" fill="none" stroke="#ffffff" stroke-width="3"/>
    </svg>
    <div class="lbl" style="left:20px;top:84px">PEOPLE<br>FORGET FAST</div>
    <div class="lbl" style="left:260px;top:177px">WITHIN A WEEK,<br>70% IS GONE</div>
  </div>
</section>

<section class="practice">
  <h2>Practice Made<br><span class="grad-text">Permanent.</span></h2>
  <p class="intro">You'll replace "hope they remember" with a system that makes sure they do.</p>
  <div class="person" role="img" aria-label="Smiling businessman in a light blazer holding a tablet, framed in a soft glowing circle"></div>
  <div class="dash" style="left:443px;top:272px;width:135px;height:100px">
    <svg width="135" height="100" viewBox="0 0 135 100">
      <rect x="6" y="6" width="36" height="6" rx="2" fill="#dbe4f2"/><rect x="48" y="6" width="36" height="6" rx="2" fill="#dbe4f2"/><rect x="110" y="6" width="19" height="8" rx="2" fill="#3f6fc4"/>
      <g fill="#3f6fc4"><rect x="48" y="42" width="4" height="14"/><rect x="55" y="36" width="4" height="20"/><rect x="62" y="30" width="4" height="26"/><rect x="69" y="26" width="4" height="30"/><rect x="76" y="22" width="4" height="34"/></g>
      <circle cx="112" cy="40" r="12" fill="none" stroke="#4cc3f0" stroke-width="4"/>
      <rect x="6" y="22" width="34" height="34" rx="3" fill="#eef3fa"/>
      <polyline points="6,92 26,80 46,86 66,72 86,78" fill="none" stroke="#4a86d6" stroke-width="2"/>
      <g fill="#3f6fc4"><rect x="100" y="70" width="4" height="4"/><rect x="110" y="80" width="4" height="4"/><rect x="120" y="66" width="4" height="4"/></g>
    </svg>
  </div>
  <div class="dash" style="left:98px;top:543px;width:117px;height:90px">
    <svg width="117" height="90" viewBox="0 0 117 90">
      <g stroke="#e3e8ef"><path d="M6 20H111M6 35H111M6 50H111"/></g>
      <path d="M6 48 C25 20 40 20 55 38 C70 52 85 14 111 30" fill="none" stroke="#4a86d6" stroke-width="2"/>
      <path d="M6 50 C30 36 50 44 70 46 C85 48 100 40 111 44" fill="none" stroke="#4cc3f0" stroke-width="1.5"/>
      <g fill="#dbe4f2"><rect x="6" y="62" width="30" height="5" rx="2"/><rect x="44" y="62" width="30" height="5" rx="2"/><rect x="82" y="62" width="29" height="5" rx="2"/></g>
      <g fill="#3f6fc4"><rect x="6" y="74" width="18" height="5" rx="2"/><rect x="44" y="74" width="22" height="5" rx="2"/><rect x="82" y="74" width="14" height="5" rx="2"/></g>
    </svg>
  </div>
  <svg style="position:absolute;left:560px;top:250px" width="140" height="440" viewBox="0 0 140 440">
    <g fill="none" stroke="#7fb7e6" stroke-width="3" stroke-dasharray="2 5" stroke-linecap="round">
      <path d="M0 232 C60 232 60 60 130 30"/>
      <path d="M0 232 H130"/>
      <path d="M0 232 C60 232 60 400 130 420"/>
    </g>
  </svg>
  <div class="card" style="top:250px">
    <div class="icon"><svg width="44" height="44" viewBox="0 0 44 44" fill="none" stroke="#fff" stroke-width="2"><circle cx="22" cy="22" r="15"/><path d="M22 7v30M9 16h26M9 28h26"/></svg></div>
    <h3>LEARN</h3>
    <p>Fast, focused workshops, built on science, that install the mindset and skills that matter most.</p>
  </div>
  <div class="card" style="top:402px">
    <div class="icon"><svg width="44" height="44" viewBox="0 0 44 44" fill="none" stroke="#fff" stroke-width="2"><circle cx="22" cy="22" r="15"/><circle cx="22" cy="22" r="6"/><path d="M22 7v9M22 28v9M7 22h9M28 22h9"/></svg></div>
    <h3>CERTIFY</h3>
    <p>Programmatic AI-driven practice and feedback - mastery without management overhead.</p>
  </div>
  <div class="card" style="top:553px">
    <div class="icon"><svg width="44" height="44" viewBox="0 0 44 44" fill="none" stroke="#fff" stroke-width="2"><rect x="8" y="9" width="28" height="26" rx="3"/><path d="M14 29v-6M20 29v-10M26 29v-4M32 29v-12"/></svg></div>
    <h3>SUSTAIN</h3>
    <p>Light-touch challenges and dashboards that keep skills sharp long after training ends.</p>
  </div>
</section>

<section class="team">
  <div class="team-photo" role="img" aria-label="Two smiling colleagues working together at a laptop in a bright office"></div>
  <h2>Built by people who've led<br><span class="grad-text">the change themselves.</span></h2>
  <p>Behind Brightmoor Labs are leaders who've lived the challenge of making learning last. They've scaled companies, built cultures, and led transformation — and now they've designed the system they always wished existed.</p>
  <span class="btn" style="left:138px;top:439px;width:195px;height:47px">Meet the Team</span>
  <div class="divider"></div>
</section>

<section class="cta">
  <div role="img" aria-label="Flowing wave of glowing blue particles" style="position:absolute;left:0;top:250px;width:1200px;height:311px;background:radial-gradient(ellipse at 60% 70%,rgba(90,170,240,.45),transparent 60%)"></div>
  <h2>Ready to see what lasting<br>Capability looks like?</h2>
  <span class="btn" style="left:500px;top:263px;width:230px;height:55px;font-size:15px;text-transform:none">Start a Conversion</span>
</section>

<footer class="footer">
  <div class="brand"><span class="mark"></span>Brightmoor Labs</div>
  <p class="tag">Making learning that sticks through AI-driven sustainment and behavioral science.</p>
  <p class="copy">© 2024 Brightmoor Labs. All rights reserved.</p>
  <h4 style="left:507px;top:105px">NAVIGATION</h4>
  <ul style="left:509px;top:140px"><li>Home</li><li>Approach</li><li>Programs</li><li>About</li><li>Contact</li></ul>
  <h4 style="left:687px;top:105px">CONTACT US</h4>
  <ul class="contact" style="left:687px;top:145px">
    <li><svg width="18" height="14" viewBox="0 0 18 14"><rect x="1" y="1" width="16" height="12" rx="1" fill="none" stroke="#fff" stroke-width="1.5"/><path d="M1 2l8 6 8-6" fill="none" stroke="#fff" stroke-width="1.5"/></svg>contact@brightmoorlabs.com</li>
    <li><svg width="18" height="16" viewBox="0 0 18 16"><path d="M4 1l3 3-2 2c1 2 3 4 5 5l2-2 3 3-2 3C7 15 2 9 1 3z" fill="none" stroke="#fff" stroke-width="1.5"/></svg>+1 (555) 014-2290</li>
    <li><svg width="18" height="20" viewBox="0 0 18 20"><path d="M9 19s7-7 7-11A7 7 0 0 0 2 8c0 4 7 11 7 11z" fill="#fff"/><circle cx="9" cy="8" r="2.5" fill="#0e1d3d"/></svg>4820 Canyon Ridge Rd Suite 210<br>Mesa Verde, AZ 85099</li>
  </ul>
  <h4 style="left:955px;top:100px">FOLLOW US</h4>
  <div class="social"><span></span><span></span><span></span></div>
</footer>

</body>
</html>
```